Tri-Fold Menu of Services for our Eyelash and Skin Care Spa

We need a beautiful spa service menu for our upscale spa in St. Charles Missouri. We specialize in providing treatments that are specific to the clients needs. Our services are eyelash extensions, skin care treatments, full body waxing and makeup application. Our spa colors are dark purples and greys and we are not opposed to additional colors that would complement those colors. We do a lot of eyelash extensions and while we do what those services listed we would like the skin care treatments to be in an area that would be noticed first. One of the attachments lists all of our services, descriptions and prices (please be sure to include all services and pricing. descriptions if possible). And our website has more information about us if needed. The website was not professionally done. So it DOESN'T represent our style exactly.

I HAVE ATTACHED A FEW PHOTOS BUT THEY DON'T HAVE TO BE USED.

Target Market(s)

women who would like to look their best, 35-55, annual income of 100,000+, she is usually busy and her children (if she has any) are high school age or older.

Industry/Entity Type

It Service

Font styles to use
Serif
Sans Serif

Requirements
Must have
• Must list all of our services. If it works to have the descriptions that would be great.
Nice to have
• If it works to have the descriptions of each service that would be great.

```html
<!DOCTYPE html>
<html lang="en">
<head>
<meta charset="utf-8">
<title>Lumera Lash &amp; Skin Spa – Service Menu</title>
<link href="https://fonts.googleapis.com/css2?family=Source+Sans+3:wght@400;600;700&display=swap" rel="stylesheet">
<style>
:root{
  --plum:#3a0838;
  --violet:#7a4a9a;
  --panel-grey:#e6e6e8;
  --ink:#1d1d1d;
  --white:#ffffff;
  --hair:#c8c8cc;
}
*{margin:0;padding:0;box-sizing:border-box}
html,body{width:1200px;height:848px;overflow:hidden;background:var(--white)}
body{font-family:"Source Sans 3",Arial,sans-serif;color:var(--ink)}
.brochure{position:relative;width:1200px;height:848px;overflow:hidden}

/* Left panel – treatments */
.panel-services{position:absolute;left:0;top:0;width:399px;height:848px;background:var(--panel-grey)}
.section-tab{position:absolute;left:0;font-size:17px;font-weight:700;color:var(--violet);padding-left:22px;border-bottom:2px solid var(--violet);width:100px;padding-bottom:2px}
.peel{position:absolute;left:16px;width:372px}
.peel-head{display:flex;font-size:17px;font-weight:600;color:var(--violet);line-height:20px}
.peel-name{flex:1}
.peel-price{color:var(--ink);width:200px;white-space:nowrap}
.peel-desc{font-size:13px;line-height:16px;color:var(--ink)}
.addons-title{position:absolute;left:0;top:318px;width:399px;text-align:center;font-size:17px;font-weight:600;color:var(--violet)}
.addon-list{position:absolute;left:16px;top:342px;width:366px;list-style:none}
.addon-list li{display:flex;justify-content:space-between;font-size:17px;font-weight:600;line-height:23px;color:var(--violet)}
.addon-list li span:last-child{color:var(--ink)}
.lash-tab{top:563px;width:106px;padding-left:16px}
.lash-group{position:absolute;left:18px;width:160px}
.lash-group h3{font-size:16px;font-weight:600;color:var(--violet);line-height:20px}
.lash-row{display:flex;justify-content:space-between;font-size:15px;font-weight:600;line-height:21px;padding-left:8px;width:158px}
.lash-gallery{position:absolute;left:185px;top:588px;width:222px;height:260px;background:var(--white);padding:8px 10px 0 10px}
.lash-photo{display:block;width:202px;height:76px;margin-bottom:7px}

/* Middle panel – about, contact, hours */
.panel-about{position:absolute;left:399px;top:0;width:399px;height:848px;background:var(--plum);color:var(--white)}
.about-title{position:absolute;left:24px;top:20px;font-size:17px;font-weight:700;border-bottom:2px solid var(--white);padding-bottom:2px;width:90px}
.about-copy{position:absolute;left:24px;width:358px;font-size:13px;line-height:19px}
.block-title{position:absolute;left:0;width:399px;text-align:center;font-size:17px}
.block-title::after{content:"";display:block;width:96px;height:1px;background:var(--white);margin:3px auto 0}
.contact{position:absolute;left:0;top:528px;width:399px;text-align:center;font-size:16px;line-height:23px}
.contact strong{font-weight:700}
.contact .addr{padding-left:20px;text-align:left;display:inline-block}
.hours{position:absolute;left:36px;top:708px;font-size:16px;font-weight:700;line-height:21.5px;border-collapse:collapse}
.hours td{padding:0}
.hours td:first-child{width:166px}

/* Right panel – cover */
.panel-cover{position:absolute;left:798px;top:0;width:402px;height:848px;background:var(--white)}
.cover-photo{position:absolute;left:0;top:0}
.brand{position:absolute;left:50px;top:668px;color:var(--plum);display:flex;align-items:center;gap:12px}
.brand-dot{width:18px;height:18px;border-radius:50%;background:var(--plum)}
.brand-name{font-size:56px;font-weight:400;line-height:1;letter-spacing:1px}
.brand-tag{position:absolute;left:150px;top:738px;font-size:19px;color:var(--plum)}
.website{position:absolute;left:0;top:808px;width:402px;text-align:center;font-size:16px;color:#333}
</style>
</head>
<body>
<main class="brochure">

  <section class="panel-services">
    <h2 class="section-tab" style="top:18px">Peels</h2>

    <div class="peel" style="top:54px">
      <div class="peel-head"><span class="peel-name">Acne Lift Peel</span><span class="peel-price">$50/1&nbsp; $250/6&nbsp; 30 minutes</span></div>
      <p class="peel-desc">Mild to moderate Acne peel</p>
    </div>
    <div class="peel" style="top:102px">
      <div class="peel-head"><span class="peel-name">Lightening Lift Peel</span><span class="peel-price">$50/1&nbsp; $250/6&nbsp; 30 minutes</span></div>
      <p class="peel-desc">Pigmentation (sun/brown spots), uneven skin tone</p>
    </div>
    <div class="peel" style="top:153px">
      <div class="peel-head"><span class="peel-name">Wrinkle Lift</span><span class="peel-price">$50/1&nbsp; $250/6&nbsp; 30 minutes</span></div>
      <p class="peel-desc">Aging, fine lines and wrinkles</p>
    </div>
    <div class="peel" style="top:200px">
      <div class="peel-head"><span class="peel-name">Signature Lift</span><span class="peel-price">$50/1&nbsp; $250/6&nbsp; 30 minutes</span></div>
      <p class="peel-desc">Rosacea, dry/dehydrated</p>
    </div>
    <div class="peel" style="top:247px">
      <div class="peel-head"><span class="peel-name">Perfection Lift</span><span class="peel-price">$100/1&nbsp; $350/4&nbsp; 30 minutes</span></div>
      <p class="peel-desc">Advanced Aging, Acne, and Pigmentation (slightly more aggressive than the other options)</p>
    </div>

    <h2 class="addons-title">Add Ons</h2>
    <ul class="addon-list">
      <li><span>Microdermabrasion</span><span>$30</span></li>
      <li><span>Firming Lift &amp; Glow Eye Treatment</span><span>$20</span></li>
      <li><span>Hot or Cold Stones</span><span>$15</span></li>
      <li><span>Extended Massage</span><span>$15</span></li>
      <li><span>Peppermint Scalp Massage</span><span>$15</span></li>
      <li><span>Foot Scrub &amp; Massage</span><span>$20</span></li>
      <li><span>Aromatherapy</span><span>$10</span></li>
      <li><span>Specialty Ampoule</span><span>$15</span></li>
      <li><span>Specialty Mask</span><span>$13</span></li>
    </ul>

    <h2 class="section-tab lash-tab">EYELASHES</h2>
    <div class="lash-group" style="top:612px">
      <h3>Classic</h3>
      <div class="lash-row"><span>Full Set</span><span>175</span></div>
      <div class="lash-row"><span>Demi Set</span><span>110</span></div>
      <div class="lash-row"><span>Touch up</span><span>60</span></div>
    </div>
    <div class="lash-group" style="top:696px">
      <h3>Volume Technique</h3>
      <div class="lash-row"><span>Full Set</span><span>220</span></div>
      <div class="lash-row"><span>Demi Set</span><span>135</span></div>
      <div class="lash-row"><span>Touch up</span><span>72</span></div>
    </div>

    <div class="lash-gallery">
      <svg class="lash-photo" role="img" aria-label="Close-up photo of an open eye with classic lash extensions" viewBox="0 0 202 76"><defs><linearGradient id="skinA" x1="0" x2="0" y1="0" y2="1"><stop offset="0" stop-color="#c9a08c"/><stop offset="1" stop-color="#a87866"/></linearGradient></defs><rect width="202" height="76" fill="url(#skinA)"/></svg>
      <svg class="lash-photo" role="img" aria-label="Close-up photo of a closed eye with full lash extensions" viewBox="0 0 202 76"><rect width="202" height="76" fill="url(#skinA)"/></svg>
      <svg class="lash-photo" role="img" aria-label="Close-up photo of an open eye with volume lash extensions" viewBox="0 0 202 76"><rect width="202" height="76" fill="url(#skinA)"/></svg>
    </div>
  </section>

  <section class="panel-about">
    <h2 class="about-title">About Us</h2>
    <p class="about-copy" style="top:56px">We specialize in providing treatments that are specific to the clients needs. Our services are eyelash extensions, skin care treatments, full body waxing and makeup application.</p>
    <p class="about-copy" style="top:155px">We specialize in providing treatments that are specific to the clients needs. Our services are eyelash extensions, skin care treatments, full body waxing and makeup application.</p>
    <p class="about-copy" style="top:255px">We specialize in providing treatments that are specific to the clients needs. Our services are eyelash extensions, skin care treatments, full body waxing and makeup application.</p>

    <h2 class="block-title" style="top:492px">Contact Us</h2>
    <address class="contact" style="font-style:normal">
      <span class="addr"><strong>2450 Linden Grove Rd</strong><br><strong>Harlow Springs, MO 63390</strong></span><br>
      phone: <strong>636-555-0142</strong><br>
      email:&nbsp; <strong>hello@lumeraspa.com</strong>
    </address>

    <h2 class="block-title" style="top:670px">Time:</h2>
    <table class="hours">
      <tr><td>Tuesday</td><td>11:00am - 6:00pm</td></tr>
      <tr><td>Wednesday-Friday</td><td>11:00am - 8:00pm</td></tr>
      <tr><td>Saturday</td><td>10:00am - 3:00pm</td></tr>
      <tr><td>Sunday-Monday</td><td>Closed</td></tr>
    </table>
  </section>

  <section class="panel-cover">
    <svg class="cover-photo" width="402" height="640" viewBox="0 0 402 640">
      <defs>
        <linearGradient id="hairTone" x1="0" x2="1" y1="0" y2="1">
          <stop offset="0" stop-color="#f2ece8"/>
          <stop offset="0.45" stop-color="#b77a4e"/>
          <stop offset="1" stop-color="#e8d6c8"/>
        </linearGradient>
      </defs>
      <path d="M0 0H402V500Q220 540 0 626Z" fill="url(#hairTone)" role="img" aria-label="Portrait photo of a smiling woman with long wavy auburn hair"/>
      <path d="M0 626Q220 540 402 500" fill="none" stroke="var(--plum)" stroke-width="6"/>
    </svg>
    <div class="brand"><span class="brand-dot"></span><span class="brand-name">Lumera</span></div>
    <div class="brand-tag">Lash &amp; Skin Spa</div>
    <p class="website">www.lumeraspa.com</p>
  </section>

</main>
</body>
</html>
```